Velmora Water Purification

We need a website set up on a "Free account" WordPress platform. (This is the type of Wordpress site that you can sign up for and create online for free (not a server-hosted type.)
The website will be for a water purification company. They install devices in homes to purify the water for safer drinking, bathing, and cleaning.
Our logo is attached. Please keep color scheme of the website consistent with the logo.
Water Purification

```html
<!DOCTYPE html>
<html lang="en">
<head>
<meta charset="utf-8">
<title>Velmora Water Purification</title>
<link href="https://fonts.googleapis.com/css2?family=Lobster+Two:ital,wght@1,700&family=Open+Sans:wght@400;600;700&display=swap" rel="stylesheet">
<style>
:root{
  --navy:#1e2a78;
  --navy-dark:#18215e;
  --blue:#1a8fd6;
  --sky:#3fb1ea;
  --pale:#e8f5fc;
  --text:#555d6b;
  --white:#ffffff;
}
*{margin:0;padding:0;box-sizing:border-box}
html,body{width:1200px;height:4144px;overflow:hidden}
body{position:relative;font-family:"Open Sans",sans-serif;color:var(--text);background:var(--white)}
.abs{position:absolute}
.script{font-family:"Lobster Two",cursive;font-style:italic;font-weight:700}
.btn{position:absolute;display:flex;align-items:center;justify-content:space-between;height:50px;padding:0 6px 0 26px;border-radius:25px;background:var(--navy);color:var(--white);font-weight:700;font-size:15px;letter-spacing:1px}
.btn .drop{width:38px;height:38px;border-radius:50%;background:var(--white);display:flex;align-items:center;justify-content:center}
.placeholder{position:absolute}

/* top bar & nav */
.topbar{left:0;top:0;width:1200px;height:32px;display:flex;justify-content:flex-end;align-items:center;gap:16px;padding-right:40px;font-size:13px;color:var(--navy)}
.topbar .phone{display:flex;align-items:center;gap:6px;font-weight:700}
.brand{left:110px;top:40px;display:flex;align-items:center;gap:12px;color:var(--navy);font-weight:700;font-size:26px}
.brand .mark{width:56px;height:56px;border-radius:50%;background:var(--blue)}
.nav{right:40px;top:76px;display:flex;gap:30px;font-size:14px;font-weight:600;color:var(--navy)}
.nav .active{color:var(--blue)}

/* hero */
.hero-bg{left:0;top:0;width:1200px;height:840px;background:linear-gradient(180deg,#ffffff 0%,#f1f8fd 55%,#d9effb 100%);z-index:-1}
.hero-family{left:40px;top:120px;width:560px;height:420px;border-radius:8px;background:radial-gradient(ellipse at 50% 45%,#f3e2d3 0%,#d7e9f6 70%,#eef7fc 100%)}
.hero-purifier{left:830px;top:110px;width:300px;height:440px;border-radius:8px;background:linear-gradient(180deg,#cfe8f8 0%,#6fb9e6 55%,#2a7ec4 100%)}
.hero-wave{left:0;top:500px;width:1200px;height:340px;background:linear-gradient(180deg,rgba(63,177,234,0) 0%,#5bbcee 35%,#1a8fd6 100%)}
.hero-dots{left:1150px;top:350px;display:flex;flex-direction:column;gap:14px}
.hero-dots span{width:12px;height:12px;border-radius:50%;border:2px solid var(--navy)}
.hero-dots .on{background:var(--navy)}
.hero-name{left:0;top:600px;width:1200px;text-align:center;color:var(--white);font-size:40px;font-weight:700}
.hero-tag{left:430px;top:672px;width:340px;text-align:center;color:var(--white);font-size:18px;line-height:28px;font-weight:600}

/* welcome */
.section-title{font-size:42px;color:var(--navy)}
.welcome-title{left:0;top:880px;width:1200px;text-align:center}
.welcome-sub{left:0;top:936px;width:1200px;text-align:center;font-size:13px;font-weight:700;letter-spacing:2px;color:var(--blue)}
.welcome-copy{left:100px;top:976px;width:1000px;font-size:14px;line-height:26px;text-align:left}
.welcome-copy p{margin-bottom:12px}

/* services */
.services-img{left:60px;top:1260px;width:500px;height:520px;border-radius:8px;background:linear-gradient(160deg,#f5fafd 0%,#d4e9f7 50%,#9fcbe9 100%)}
.services-title{left:560px;top:1290px}
.services-lead{left:560px;top:1352px;width:580px;font-size:32px;line-height:42px;font-weight:700;color:var(--blue)}
.services-copy{left:560px;top:1460px;width:580px;font-size:14px;line-height:26px}
.services-copy p{margin-bottom:12px}

/* testimonial */
.testi-band{left:0;top:1848px;width:1200px;height:512px;background:linear-gradient(90deg,#2d7fbf 0%,#4aa8dd 55%,#9fd2ef 100%)}
.testi-photo{left:640px;top:1848px;width:560px;height:512px;background:linear-gradient(90deg,rgba(159,210,239,0) 0%,#cfe6f4 40%,#e6d2c3 75%,#c9e2f2 100%)}
.testi-quote{left:90px;top:1990px;width:420px;color:var(--white);font-size:15px;line-height:28px;font-weight:600}
.testi-q{position:absolute;font-family:Georgia,serif;font-size:54px;line-height:1;color:var(--navy);font-weight:700}
.testi-name{left:120px;top:2180px;color:var(--white);font-size:16px}
.testi-dots{left:120px;top:2230px;display:flex;gap:10px}
.testi-dots span{width:12px;height:12px;border-radius:50%;border:2px solid var(--white)}
.testi-dots .on{background:var(--white)}

/* call to action */
.cta-line{left:0;top:2410px;width:1200px;text-align:center;font-size:21px;font-weight:700;color:#2a2f45}
.cta-phone{left:0;top:2450px;width:1200px;text-align:center;font-size:64px;line-height:84px;color:var(--navy);font-style:italic;font-weight:600;letter-spacing:4px}
.rule{left:80px;top:2640px;width:1040px;height:2px;background:var(--sky)}

/* news */
.news-title{left:80px;top:2680px}
.arrow{top:2680px;width:50px;height:50px;border-radius:50%;background:var(--navy);display:flex;align-items:center;justify-content:center}
.card{top:2760px;width:330px}
.card .photo{width:330px;height:230px;background:linear-gradient(160deg,#e9f2f8 0%,#b9d6ea 60%,#7fb1d6 100%);position:relative}
.card .date{position:absolute;left:0;top:0;width:90px;height:100px;background:var(--blue);color:var(--white);text-align:center;padding-top:6px}
.card .date b{display:block;font-size:42px;line-height:50px}
.card .date span{font-size:12px}
.card p{margin-top:18px;font-size:14px;line-height:24px;color:#333}
.card a{color:var(--blue);text-decoration:none;font-weight:600}

/* contact */
.contact-bg{left:0;top:3140px;width:1200px;height:640px;background:linear-gradient(180deg,#4aa3d8 0%,#1e6fae 55%,#15508a 100%)}
.contact-glass{left:60px;top:3160px;width:360px;height:600px;background:linear-gradient(180deg,rgba(255,255,255,.28) 0%,rgba(255,255,255,.08) 100%);border-radius:6px}
.contact-title{left:0;top:3190px;width:1200px;text-align:center;color:var(--white)}
.contact-copy{left:250px;top:3258px;width:700px;text-align:center;color:var(--white);font-size:14px;line-height:24px}
.contact-ask{left:0;top:3318px;width:1200px;text-align:center;color:var(--white);font-size:17px;font-weight:600}
.field{left:290px;width:620px;height:44px;background:var(--white);border-radius:3px;font-size:14px;color:#888;padding:12px 14px}
.field.msg{height:110px}

/* footer */
.footer{left:0;top:3780px;width:1200px;height:300px;background:var(--navy-dark)}
.fcol{top:3815px;color:#cdd3f0;font-size:14px;line-height:24px}
.fcol h4{color:var(--sky);font-size:14px;letter-spacing:1px;margin-bottom:14px}
.fcol li{list-style:none;display:flex;align-items:center;gap:10px;margin-bottom:4px}
.fcol li::before{content:"";width:6px;height:6px;background:var(--sky)}
.fcol .row{display:flex;align-items:flex-start;gap:10px;margin-bottom:10px}
.icon{flex:0 0 auto;margin-top:4px}
.social{display:flex;align-items:center;gap:12px;margin-bottom:14px}
.social .c{width:36px;height:36px;border-radius:50%;background:var(--blue)}
.copybar{left:0;top:4080px;width:1200px;height:64px;background:#121a4d;color:#aeb6de;font-size:13px;display:flex;align-items:center;justify-content:center}
</style>
</head>
<body>

<!-- hero -->
<div class="abs hero-bg"></div>
<div class="placeholder hero-family" role="img" aria-label="Smiling family of three enjoying clean water"></div>
<div class="placeholder hero-purifier" role="img" aria-label="Home water purifier unit with splashing water"></div>
<div class="placeholder hero-wave" role="img" aria-label="Splashing clear blue water"></div>

<div class="abs topbar">
  <span>Call Us Today</span>
  <span class="phone">
    <svg width="14" height="14" viewBox="0 0 24 24"><path fill="#1e2a78" d="M6.6 10.8a15 15 0 0 0 6.6 6.6l2.2-2.2c.3-.3.7-.4 1-.2 1.1.4 2.3.6 3.6.6.6 0 1 .4 1 1V20c0 .6-.4 1-1 1A17 17 0 0 1 3 4c0-.6.4-1 1-1h3.5c.6 0 1 .4 1 1 0 1.3.2 2.5.6 3.6.1.3 0 .7-.2 1z"/></svg>
    123-456-7890
  </span>
</div>

<div class="abs brand"><span class="mark"></span><span>Velmora</span></div>

<nav class="abs nav">
  <span class="active">HOME</span><span>ABOUT</span><span>SERVICES</span><span>TESTIMONIALS</span><span>NEWS</span><span>CONTACT</span>
</nav>

<div class="abs hero-dots"><span></span><span></span><span></span><span class="on"></span><span></span></div>

<div class="abs hero-name">Velmora</div>
<div class="abs hero-tag">Install Devices In Homes To Purify The Water For Safer Drinking, Bathing, And Cleaning.</div>

<!-- welcome -->
<h1 class="abs section-title script welcome-title">Welcome To Velmora</h1>
<div class="abs welcome-sub">WATER PURIFICATION</div>
<div class="abs welcome-copy">
  <p>Lorem Ipsum is simply dummy text of the printing and typesetting industry. Lorem Ipsum has been the industry's standard dummy text ever since the 1500s, when an unknown printer took a galley of type and scrambled it to make.</p>
  <p>Lorem Ipsum is simply dummy text of the printing and typesetting industry. Lorem Ipsum has been the industry's standard dummy text ever since the 1500s, when an unknown printer took a galley of type and scrambled it to make a type specimen book. It has survived not only five centuries, but also the leap into electronic typesetting, remaining essentially unchanged.</p>
</div>
<div class="btn" style="left:490px;top:1130px;width:220px">LEARN MORE <span class="drop"><svg width="14" height="18" viewBox="0 0 14 18"><path fill="#1a8fd6" d="M7 0C7 0 0 8 0 11.5A7 7 0 0 0 14 11.5C14 8 7 0 7 0z"/></svg></span></div>

<!-- services -->
<div class="placeholder services-img" role="img" aria-label="Water softener and filtration units with service technicians"></div>
<h2 class="abs section-title script services-title">Services We Provide You</h2>
<div class="abs services-lead">Install Devices In Homes To Purify The Water</div>
<div class="abs services-copy">
  <p>Lorem Ipsum is simply dummy text of the printing and typesetting industry. Lorem Ipsum has been the industry's standard dummy text ever.</p>
  <p>Lorem Ipsum is simply dummy text of the printing and typesetting industry. Lorem Ipsum has been the industry's standard dummy text ever since the 1500s, when an unknown printer took a galley of type and scrambled it to make.</p>
</div>
<div class="btn" style="left:560px;top:1620px;width:220px">LEARN MORE <span class="drop"><svg width="14" height="18" viewBox="0 0 14 18"><path fill="#1a8fd6" d="M7 0C7 0 0 8 0 11.5A7 7 0 0 0 14 11.5C14 8 7 0 7 0z"/></svg></span></div>

<!-- testimonial -->
<div class="abs testi-band"></div>
<div class="placeholder testi-photo" role="img" aria-label="Woman drinking a glass of purified water in a bright kitchen"></div>
<span class="testi-q" style="left:80px;top:1990px">&ldquo;</span>
<div class="abs testi-quote" style="padding-left:40px">Lorem Ipsum is simply dummy text of the printing and typesetting industry. Lorem Ipsum has been the industry's standard dummy text ever since the 1500s, when an unknown printer took a galley of type and scrambled it to make a type specimen book.</div>
<span class="testi-q" style="left:500px;top:2110px">&rdquo;</span>
<div class="abs testi-name">&mdash; <span class="script">Client Name</span></div>
<div class="abs testi-dots"><span class="on"></span><span></span><span></span><span></span></div>

<!-- call to action -->
<div class="abs cta-line">Get Water Purification system Installation in Your Home by giving missed on :</div>
<div class="abs cta-phone">123 456 7890</div>
<div class="btn" style="left:490px;top:2555px;width:220px">CONTACT US <span class="drop"><svg width="14" height="18" viewBox="0 0 14 18"><path fill="#1a8fd6" d="M7 0C7 0 0 8 0 11.5A7 7 0 0 0 14 11.5C14 8 7 0 7 0z"/></svg></span></div>
<div class="abs rule"></div>

<!-- news -->
<h2 class="abs section-title script news-title">Latest News</h2>
<div class="abs arrow" style="left:1000px"><svg width="14" height="16" viewBox="0 0 14 16"><path d="M10 2L4 8l6 6" stroke="#fff" stroke-width="3" fill="none"/></svg></div>
<div class="abs arrow" style="left:1066px"><svg width="14" height="16" viewBox="0 0 14 16"><path d="M4 2l6 6-6 6" stroke="#fff" stroke-width="3" fill="none"/></svg></div>

<article class="abs card" style="left:80px">
  <div class="photo" role="img" aria-label="Technician installing a water filter"><div class="date"><b>16</b><span>November</span></div></div>
  <p>Lorem Ipsum is the simply dummy text of the printing and typesetting industry Lorem Ipsum is the simply dummy text <a>Read More &raquo;</a></p>
</article>
<article class="abs card" style="left:435px">
  <div class="photo" role="img" aria-label="Service expert standing beside a purification unit"><div class="date"><b>15</b><span>November</span></div></div>
  <p>Lorem Ipsum is the simply dummy text of the printing and typesetting industry Lorem Ipsum is the simply dummy text <a>Read More &raquo;</a></p>
</article>
<article class="abs card" style="left:790px">
  <div class="photo" role="img" aria-label="Woman filling a glass from a kitchen purifier"><div class="date"><b>14</b><span>November</span></div></div>
  <p>Lorem Ipsum is the simply dummy text of the printing and typesetting industry Lorem Ipsum is the simply dummy text <a>Read More &raquo;</a></p>
</article>

<!-- contact -->
<div class="placeholder contact-bg" role="img" aria-label="Glass of water against a blue lake and sky"></div>
<div class="abs contact-glass"></div>
<h2 class="abs section-title script contact-title">Contact Us</h2>
<div class="abs contact-copy">Lorem Ipsum is simply dummy text of the printing and typesetting industry. Lorem Ipsum has been the industry's standard dummy text ever.</div>
<div class="abs contact-ask">Need a free quote, or have a question? Get in touch</div>
<div class="abs field" style="top:3370px">Name *</div>
<div class="abs field" style="top:3430px">Email *</div>
<div class="abs field" style="top:3490px">Phone *</div>
<div class="abs field msg" style="top:3550px">Message *</div>
<div class="btn" style="left:540px;top:3684px;width:170px">SUBMIT <span class="drop"><svg width="14" height="18" viewBox="0 0 14 18"><path fill="#1a8fd6" d="M7 0C7 0 0 8 0 11.5A7 7 0 0 0 14 11.5C14 8 7 0 7 0z"/></svg></span></div>

<!-- footer -->
<footer class="abs footer"></footer>
<div class="abs fcol" style="left:80px;width:230px">
  <h4>ABOUT US</h4>
  <p>Lorem Ipsum is simply dummy text of the printing and typesetting industry. Lorem Ipsum has been the industry's standard dummy text.</p>
</div>
<div class="btn" style="left:80px;top:3995px;width:190px;background:var(--blue)">LEARN MORE <span class="drop"><svg width="14" height="18" viewBox="0 0 14 18"><path fill="#1e2a78" d="M7 0C7 0 0 8 0 11.5A7 7 0 0 0 14 11.5C14 8 7 0 7 0z"/></svg></span></div>
<div class="abs fcol" style="left:345px">
  <h4>SITEMAP</h4>
  <ul><li>Home</li><li>About</li><li>Services</li><li>Testimonials</li><li>News</li><li>Contact</li></ul>
</div>
<div class="abs fcol" style="left:610px;width:230px">
  <h4>CONTACT US</h4>
  <div class="row"><svg class="icon" width="12" height="16" viewBox="0 0 12 16"><path fill="#3fb1ea" d="M6 0a6 6 0 0 0-6 6c0 4.5 6 10 6 10s6-5.5 6-10a6 6 0 0 0-6-6zm0 8.5A2.5 2.5 0 1 1 6 3.5a2.5 2.5 0 0 1 0 5z"/></svg><span>Velmora<br>52 - Lorem Ipsum is the simple dummy text of print &amp; type</span></div>
  <div class="row"><svg class="icon" width="14" height="14" viewBox="0 0 24 24"><path fill="#3fb1ea" d="M6.6 10.8a15 15 0 0 0 6.6 6.6l2.2-2.2c.3-.3.7-.4 1-.2 1.1.4 2.3.6 3.6.6.6 0 1 .4 1 1V20c0 .6-.4 1-1 1A17 17 0 0 1 3 4c0-.6.4-1 1-1h3.5c.6 0 1 .4 1 1 0 1.3.2 2.5.6 3.6.1.3 0 .7-.2 1z"/></svg><span>123 - 456 - 7890</span></div>
  <div class="row"><svg class="icon" width="16" height="12" viewBox="0 0 16 12"><rect width="16" height="12" rx="1" fill="#3fb1ea"/><path d="M1 1l7 5 7-5" stroke="#18215e" stroke-width="1.5" fill="none"/></svg><span>info@velmorawater.com</span></div>
</div>
<div class="abs fcol" style="left:880px">
  <h4>FOLLOW US</h4>
  <div class="social"><span class="c"></span><span>Friendhub</span></div>
  <div class="social"><span class="c"></span><span>Chirpline</span></div>
  <div class="social"><span class="c"></span><span>WorkLink</span></div>
</div>
<div class="abs copybar">&copy;Velmora Water Purification - 2017 All Right Reserved</div>

</body>
</html>
```